www.copperleaf-nimbo.com web Page

Discover Quito Discover Otavalo Discover Cotopaxi Discover Discover Discover Mindo Birdwatching Discover Quilotoa Discover Amazonas Discover Galapagos Islands
Updates

Thank you all sending proyect designs..If you have not received a reply from us than your design has not met our original requirements .... Best Regards, Ruben

Target Market(s)

USA / Europe England,

Number of Pages Required

5+ page

Font styles to use
Sans Serif

Requirements
Must have
• I will need Logo to be upgraded instead of 17 years, it need to say 25 years. Userfriendly design, SEO friendly and responsive. Web needs to work on all devices like Android, IOS, Tablet and Windows
Nice to have
• Please consider 1. Minimalistic design 2. Copperleaf Nimbo logo in feautred areas fo web pages 3. Modular design 4. Hero not sliding images 5. Landing page with full with image 6. Elements with animations 7. Hamburger menu 8. I will drop the Packages part of www.copperleaf-nimbo.com 9. Incorporate Galapagos Islands instead 10. I will concentrate on the modular design to have Discover Quito Discover Otavalo Discover Cotopaxi Discover Discover Discover Mindo Birdwatching Discover Quilotoa Discover Amazonas Discover Galapagos Islands
Should not have
• Sliding images

```html
<!DOCTYPE html>
<html lang="en">
<head>
<meta charset="utf-8">
<title>Copperleaf Nimbo – Discover Tours</title>
<link rel="stylesheet" href="https://fonts.googleapis.com/css2?family=Roboto:wght@300;400;500;700&family=Pinyon+Script&display=swap">
<style>
:root{
  --green:#1ea84a;
  --blue:#1d46a0;
  --ink:#2b2b2b;
  --muted:#8a8a8a;
  --soft:#f4f4f4;
  --line:#e4e4e4;
  --footer:#333333;
  --footer-text:#9a9a9a;
  --white:#ffffff;
}
*{box-sizing:border-box;margin:0;padding:0}
html,body{width:1200px;height:3169px;overflow:hidden;background:#fafafa;font-family:"Roboto",Arial,sans-serif;color:var(--ink)}
.page{position:absolute;left:122px;top:70px;width:956px;height:3037px;background:var(--white);box-shadow:0 0 24px rgba(0,0,0,.08);overflow:hidden}
.abs{position:absolute}
.fill{position:absolute;inset:0}

/* hero */
.hero{left:0;top:0;width:956px;height:516px}
.hero-photo{background:linear-gradient(180deg,#c9ccd0 0%,#8d8a78 22%,#6d6a55 36%,#2f7480 50%,#3b8591 65%,#8f8260 80%,#b8a98a 100%)}
.brand{left:57px;top:36px;display:flex;align-items:center;gap:8px;color:var(--white);font-weight:700;font-size:14px;line-height:1.15;text-transform:uppercase}
.brand-dot{width:30px;height:30px;border-radius:50%;background:var(--green)}
.nav-icons{right:52px;top:38px;display:flex;gap:22px;align-items:center}
.hero-title{left:0;width:956px;top:214px;text-align:center;color:var(--white);font-size:42px;font-weight:500;letter-spacing:1px}
.hero-sub{left:0;width:956px;top:272px;text-align:center;color:var(--white);font-size:17px;font-weight:500}
.hero-actions{left:0;width:956px;top:333px;display:flex;justify-content:center;gap:16px}
.btn{display:inline-flex;align-items:center;justify-content:center;height:34px;font-size:10px;font-weight:500;text-transform:uppercase;letter-spacing:.3px}
.btn-green{width:112px;background:var(--green);color:var(--white)}
.btn-ghost{width:104px;border:1px solid var(--white);color:var(--white)}

/* category tiles */
.tile{top:533px;width:226px;height:149px}
.tile-label{position:absolute;left:24px;bottom:22px;color:var(--white);font-size:28px;font-weight:500;line-height:1;text-transform:uppercase}
.tile-label small{display:block;font-size:19px}

/* letter */
.letter-title{left:0;width:956px;top:742px;text-align:center;font-family:"Pinyon Script",cursive;font-size:26px;color:var(--ink)}
.letter-body{left:238px;width:480px;top:796px;text-align:center;font-size:11px;line-height:27px;color:var(--muted)}
.btn-grey{left:439px;top:905px;width:78px;height:26px;background:#cfcfcf;color:var(--white);font-size:8px}

/* activities */
.activities{left:0;top:1022px;width:956px;height:423px;background:var(--soft)}
.section-head{font-size:18px;font-weight:500;text-transform:uppercase;color:var(--ink)}
.section-head span{color:#a5a5a5;font-weight:400}
.activity-photo{left:85px;top:66px;width:183px;height:158px;background:linear-gradient(160deg,#e8e8e8,#8c8c8c 55%,#3a3a3a)}
.activity-name{left:300px;top:58px;font-size:16px;font-weight:500}
.activity-text{left:300px;top:92px;width:250px;font-size:11px;line-height:22px;color:var(--muted)}
.activity-price{left:300px;top:182px;font-size:11px;font-weight:500;color:var(--green)}
.pager{left:300px;top:262px;display:flex;gap:6px}
.pager-btn{width:18px;height:18px;border:1px solid #555;display:flex;align-items:center;justify-content:center}
.hot-grid{left:593px;top:66px;display:grid;grid-template-columns:133px 133px;grid-template-rows:107px 107px;gap:17px 10px}

/* discover tours */
.discover-head{left:0;width:956px;top:1472px;text-align:center}
.tour-card{top:1540px;width:218px;height:426px;background:var(--white);box-shadow:0 0 8px rgba(0,0,0,.12)}
.tour-photo{position:absolute;left:0;top:0;width:218px;height:125px}
.tour-photo-title{position:absolute;left:24px;top:52px;color:var(--white);font-size:22px;font-weight:500;line-height:26px}
.tour-body{position:absolute;left:30px;top:150px;right:16px}
.tour-city{display:flex;align-items:center;gap:10px;font-size:15px;margin-bottom:14px}
.ring{width:10px;height:10px;border:1.5px solid #9a9a9a;border-radius:50%}
.tour-list{list-style:none;padding-left:20px}
.tour-list li{display:flex;align-items:center;gap:8px;font-size:10px;color:var(--muted);height:22px}
.tour-list li small{font-size:6px}
.tour-divider{height:1px;background:var(--line);margin:14px 0 12px}
.tour-more{display:flex;align-items:center;gap:10px;font-size:13px;height:34px}

/* partner sites */
.sites{left:0;top:2087px;width:956px;height:448px;background:var(--soft)}
.site-card{top:43px;width:237px;height:330px;background:var(--white);border:1px solid var(--line)}
.site-photo{position:absolute;left:8px;top:8px;width:221px;height:142px}
.site-name{position:absolute;left:16px;top:168px;font-size:13px;font-weight:500}
.site-url{position:absolute;left:16px;top:188px;font-size:10px;color:var(--muted)}
.site-text{position:absolute;left:16px;top:206px;width:205px;font-size:10px;line-height:16px;color:var(--muted)}
.btn-blue{position:absolute;left:16px;top:281px;width:78px;height:24px;background:var(--blue);color:var(--white);font-size:9px}

/* partners */
.partners{left:0;top:2535px;width:956px;height:99px;display:flex;align-items:center;justify-content:center;gap:58px}
.partner{background:#e2e2e2}
.partners-arrow{top:2575px}

/* footer */
.skyline{left:0;top:2634px;width:956px;height:79px;background:linear-gradient(180deg,#ffffff 0%,#7a7a7a 55%,#333333 100%)}
.footer{left:0;top:2713px;width:956px;height:324px;background:var(--footer)}
.foot-col{top:66px}
.foot-head{font-size:12px;font-weight:500;color:var(--white);text-transform:uppercase;margin-bottom:22px}
.foot-list{list-style:none}
.foot-list li{font-size:10px;color:var(--footer-text);height:22px}
.field{width:164px;height:24px;border:1px solid #777;font-size:9px;color:var(--white);padding:6px 8px;margin-bottom:10px}
.field-tall{height:42px}
.btn-send{margin-left:106px;width:58px;height:16px;background:var(--green);color:var(--white);font-size:8px}
.contact-line{display:flex;gap:10px;font-size:10px;line-height:20px;color:var(--footer-text)}
.foot-rule{left:108px;top:272px;width:740px;height:1px;background:#444}
.copyright{left:0;width:956px;top:290px;text-align:center;font-size:9px;color:var(--footer-text);text-transform:uppercase}
</style>
</head>
<body>
<main class="page">

  <!-- hero -->
  <section class="abs hero">
    <div class="fill hero-photo" role="img" aria-label="Hiker with a blue backpack sitting on a crater rim above a turquoise crater lake ringed by mountains"></div>
    <div class="abs brand"><span class="brand-dot"></span><span>Copperleaf Nimbo<br>25 years</span></div>
    <div class="abs nav-icons">
      <svg width="22" height="16" viewBox="0 0 22 16" aria-label="Menu"><rect y="1" width="22" height="2.4" fill="#1d46a0"/><rect x="4" y="7" width="18" height="2.4" fill="#1d46a0"/><rect x="8" y="13" width="14" height="2.4" fill="#1d46a0"/></svg>
      <svg width="16" height="16" viewBox="0 0 24 24" aria-label="Call"><path d="M6.6 10.8a15 15 0 0 0 6.6 6.6l2.2-2.2a1 1 0 0 1 1-.25 11.4 11.4 0 0 0 3.6.6 1 1 0 0 1 1 1V20a1 1 0 0 1-1 1A17 17 0 0 1 3 4a1 1 0 0 1 1-1h3.5a1 1 0 0 1 1 1c0 1.25.2 2.45.6 3.6a1 1 0 0 1-.25 1z" fill="#1ea84a"/></svg>
    </div>
    <h1 class="abs hero-title">DISCOVER&nbsp; TOURS</h1>
    <p class="abs hero-sub">If you enjoy history and art, Quito is your perfect destination.</p>
    <div class="abs hero-actions">
      <span class="btn btn-green">Book now</span>
      <span class="btn btn-ghost">Read more</span>
    </div>
  </section>

  <!-- category tiles -->
  <a class="abs tile" style="left:0;background:linear-gradient(150deg,#7a6a4a,#3d4a2a 60%,#6b3a1e)" role="img" aria-label="Blue tropical bird perched on a branch with red berries">
    <span class="tile-label"><small>Bird watching</small>Tours</span></a>
  <a class="abs tile" style="left:243px;background:linear-gradient(170deg,#d6d6d6,#8b8b8b 60%,#4a4a4a)" role="img" aria-label="Black and white view of colonial church towers in Quito">
    <span class="tile-label">Day<br>Tours</span></a>
  <a class="abs tile" style="left:489px;background:linear-gradient(160deg,#4b6a3a,#2f4a2a 50%,#9fb2a8)" role="img" aria-label="Waterfall in green cloud forest">
    <span class="tile-label">Mindo Day<br>Tours</span></a>
  <a class="abs tile" style="left:732px;width:224px;background:linear-gradient(160deg,#5e8a4a,#2e5a2e 60%,#6a8a5a)" role="img" aria-label="Aerial view of lodges in the Amazon rainforest">
    <span class="tile-label"><small>Amazon lodges &amp;</small>Tours</span></a>

  <!-- letter -->
  <h2 class="abs letter-title">Dear Friends</h2>
  <p class="abs letter-body">Many years ago when I founded Copperleaf Nimbo Cia. Ltda. in Ecuador, my basic premise was to offer consistently high quality services from beginning to end. We want your stay in Ecuador to be one you will remember all your life.</p>
  <span class="abs btn btn-grey">Read more</span>

  <!-- activities -->
  <section class="abs activities">
    <h2 class="abs section-head" style="left:85px;top:20px">Find <span>activities</span></h2>
    <div class="abs activity-photo" role="img" aria-label="Snow-covered Antisana volcano in black and white"></div>
    <h3 class="abs activity-name">Antisana Volcano Reserve</h3>
    <p class="abs activity-text">This is a spectacular day trip out of Quito to the volcano Antisana, the fourth in altitude in Ecuador, covered with glaciers and snow, and the surrounding Ecological Reserve.</p>
    <p class="abs activity-price">Starting from USD85</p>
    <div class="abs pager">
      <span class="pager-btn"><svg width="8" height="8" viewBox="0 0 8 8"><path d="M5.5 1 2.5 4l3 3" fill="none" stroke="#333" stroke-width="1.2"/></svg></span>
      <span class="pager-btn"><svg width="8" height="8" viewBox="0 0 8 8"><path d="M2.5 1l3 3-3 3" fill="none" stroke="#333" stroke-width="1.2"/></svg></span>
    </div>
    <h2 class="abs section-head" style="left:593px;top:20px">Hot <span>tours</span></h2>
    <div class="abs hot-grid">
      <div style="background:linear-gradient(170deg,#6f9ed0,#c9b28a 55%,#7a5a3a)" role="img" aria-label="Colonial church and plaza in Quito"></div>
      <div style="background:linear-gradient(160deg,#3a4a7a,#9a3a3a 50%,#6a5a3a)" role="img" aria-label="Colourful indigenous market stall"></div>
      <div style="background:linear-gradient(180deg,#9ab0b8,#3d7a80 55%,#4a5a3a)" role="img" aria-label="Crater lake surrounded by hills"></div>
      <div style="background:linear-gradient(150deg,#6a9a3a,#2e6a2e 55%,#8ab04a)" role="img" aria-label="Green hummingbird among leaves"></div>
    </div>
  </section>

  <!-- discover tours -->
  <h2 class="abs section-head discover-head">Discover <span>tours</span></h2>

  <article class="abs tour-card" style="left:248px">
    <div class="tour-photo" style="background:linear-gradient(180deg,#8eb0d8,#e8ecf0 40%,#6a6a6a 75%,#3a3a3a)" role="img" aria-label="Snow-capped Andes peaks"></div>
    <span class="tour-photo-title">Andes<br>Tours</span>
    <div class="tour-body">
      <div class="tour-city"><span class="ring"></span>Quito</div>
      <ul class="tour-list">
        <li><svg width="9" height="8" viewBox="0 0 9 8"><path d="M1 4l2.4 2.5L8 1" fill="none" stroke="#1ea84a" stroke-width="1.4"/></svg>Quito City Tour</li>
        <li><svg width="9" height="8" viewBox="0 0 9 8"><path d="M1 4l2.4 2.5L8 1" fill="none" stroke="#1ea84a" stroke-width="1.4"/></svg>Quito Tour + Equatorial Line</li>
        <li><svg width="9" height="8" viewBox="0 0 9 8"><path d="M1 4l2.4 2.5L8 1" fill="none" stroke="#1ea84a" stroke-width="1.4"/></svg>Quito City Tour + Teleferico</li>
        <li><svg width="9" height="8" viewBox="0 0 9 8"><path d="M1 4l2.4 2.5L8 1" fill="none" stroke="#1ea84a" stroke-width="1.4"/></svg>Quito Museum Tour</li>
        <li><svg width="9" height="8" viewBox="0 0 9 8"><path d="M1 4l2.4 2.5L8 1" fill="none" stroke="#1ea84a" stroke-width="1.4"/></svg>Quito - Pasochoa</li>
      </ul>
      <div class="tour-divider"></div>
      <div class="tour-more"><span class="ring"></span>Discover Otavalo</div>
      <div class="tour-more"><span class="ring"></span>Discover Cotopaxi</div>
    </div>
  </article>

  <article class="abs tour-card" style="left:493px;width:220px">
    <div class="tour-photo" style="width:220px;background:linear-gradient(160deg,#4a5a3a,#2a3a22 50%,#8a8a6a)" role="img" aria-label="Dense jungle trail with tall trees"></div>
    <span class="tour-photo-title">Jungle<br>Tours</span>
    <div class="tour-body">
      <div class="tour-city"><span class="ring"></span>Mindo</div>
      <ul class="tour-list">
        <li><svg width="9" height="8" viewBox="0 0 9 8"><path d="M1 4l2.4 2.5L8 1" fill="none" stroke="#1ea84a" stroke-width="1.4"/></svg>Mindo Tour <small>(optional Bellavista Reserve)</small></li>
        <li><svg width="9" height="8" viewBox="0 0 9 8"><path d="M1 4l2.4 2.5L8 1" fill="none" stroke="#1ea84a" stroke-width="1.4"/></svg>Tulipe Trekking</li>
        <li><svg width="9" height="8" viewBox="0 0 9 8"><path d="M1 4l2.4 2.5L8 1" fill="none" stroke="#1ea84a" stroke-width="1.4"/></svg>Nono-Tandayapa</li>
        <li><svg width="9" height="8" viewBox="0 0 9 8"><path d="M1 4l2.4 2.5L8 1" fill="none" stroke="#1ea84a" stroke-width="1.4"/></svg>Mindo Tour 2D/1N</li>
        <li><svg width="9" height="8" viewBox="0 0 9 8"><path d="M1 4l2.4 2.5L8 1" fill="none" stroke="#1ea84a" stroke-width="1.4"/></svg>Bellavista Reserve 2D/1N</li>
      </ul>
      <div class="tour-divider"></div>
      <div class="tour-more"><span class="ring"></span>Discover Amazonas</div>
      <div class="tour-more"><span class="ring"></span>Discover Galapagos</div>
    </div>
  </article>

  <!-- partner sites -->
  <section class="abs sites">
    <article class="abs site-card" style="left:116px">
      <div class="site-photo" style="background:linear-gradient(170deg,#8aa8c8,#6a5a4a 50%,#3a2a22)" role="img" aria-label="Lodge lounge with sofas and panoramic windows over the city"></div>
      <h3 class="site-name">Alderview Lodge</h3>
      <p class="site-url">www.alderview-lodge.com</p>
      <p class="site-text">Our guest house was built with the idea for you to enjoy one of the most breathtaking panoramic views of the city of Quito...</p>
      <span class="btn btn-blue">View site</span>
    </article>
    <article class="abs site-card" style="left:362px">
      <div class="site-photo" style="background:linear-gradient(160deg,#4a6a3a,#c8d0c8 50%,#2e4a2a)" role="img" aria-label="Waterfall in cloud forest"></div>
      <h3 class="site-name">Veranube Cloud Forest</h3>
      <p class="site-url">www.veranube-reserve.org</p>
      <p class="site-text">Friends of the Veranube Woods (Friends of the Veranube Cloud Forest) was established in 2004. The main objective...</p>
      <span class="btn btn-blue">View site</span>
    </article>
    <article class="abs site-card" style="left:607px">
      <div class="site-photo" style="background:linear-gradient(180deg,#2a6aa8,#1a4a80 60%,#123a66)" role="img" aria-label="Diver swimming beside a whale shark"></div>
      <h3 class="site-name">Isla Verde Voyages</h3>
      <p class="site-url">www.islaverde-voyages.com</p>
      <p class="site-text">Ecuador and the Galapagos have unique positions geographically and geologically in the world, which all contribute to their climates...</p>
      <span class="btn btn-blue">View site</span>
    </article>
  </section>

  <!-- partners -->
  <svg class="abs partners-arrow" style="left:80px" width="12" height="18" viewBox="0 0 12 18" aria-label="Previous"><path d="M9 2 3 9l6 7" fill="none" stroke="#333" stroke-width="2"/></svg>
  <div class="abs partners">
    <span class="partner" style="width:62px;height:52px;border-radius:50%"></span>
    <span class="partner" style="width:90px;height:44px"></span>
    <span class="partner" style="width:40px;height:52px"></span>
    <span class="partner" style="width:120px;height:30px"></span>
    <span class="partner" style="width:104px;height:46px"></span>
  </div>
  <svg class="abs partners-arrow" style="left:866px" width="12" height="18" viewBox="0 0 12 18" aria-label="Next"><path d="M3 2l6 7-6 7" fill="none" stroke="#bbb" stroke-width="2"/></svg>

  <!-- footer -->
  <div class="abs skyline" role="img" aria-label="Dark silhouette of trees, mountains and church towers"></div>
  <footer class="abs footer">
    <div class="abs foot-col" style="left:108px">
      <h4 class="foot-head">Quick links</h4>
      <ul class="foot-list"><li>Home</li><li>Bird Watching Tour</li><li>Day Tours</li><li>Mindo Day Tours</li><li>Amazon Lodges &amp; Tours</li><li>Contact Us</li></ul>
    </div>
    <div class="abs foot-col" style="left:296px">
      <h4 class="foot-head">Ecuador FAQ</h4>
      <ul class="foot-list"><li>About Ecuador</li><li>Tips for the Tourist</li><li>Experiences</li><li>Memories</li><li>Connectivity</li></ul>
    </div>
    <div class="abs foot-col" style="left:455px">
      <h4 class="foot-head">Contact form</h4>
      <div class="field">Name</div>
      <div class="field">Email Address</div>
      <div class="field field-tall">Message</div>
      <span class="btn btn-send">Send</span>
    </div>
    <div class="abs foot-col" style="left:684px">
      <h4 class="foot-head">Contact us</h4>
      <p class="contact-line">Main Office</p>
      <p class="contact-line">Calle Los Alisos 12-40 y<br>Olmedo, Quito</p>
      <p class="contact-line" style="margin-top:6px"><svg width="9" height="10" viewBox="0 0 24 24"><path d="M6.6 10.8a15 15 0 0 0 6.6 6.6l2.2-2.2a1 1 0 0 1 1-.25 11.4 11.4 0 0 0 3.6.6 1 1 0 0 1 1 1V20a1 1 0 0 1-1 1A17 17 0 0 1 3 4a1 1 0 0 1 1-1h3.5a1 1 0 0 1 1 1c0 1.25.2 2.45.6 3.6a1 1 0 0 1-.25 1z" fill="#9a9a9a"/></svg>593-2-000 4817</p>
      <p class="contact-line"><svg width="10" height="10" viewBox="0 0 10 8" style="margin-top:6px"><rect x=".5" y=".5" width="9" height="7" fill="none" stroke="#9a9a9a"/><path d="M.5.5 5 4.5 9.5.5" fill="none" stroke="#9a9a9a"/></svg>info@copperleaf-nimbo.com</p>
    </div>
    <div class="abs foot-rule"></div>
    <p class="abs copyright">©Copperleaf Nimbo 2005. All Rights Reserved</p>
  </footer>

</main>
</body>
</html>
```